Jewelry Shop Needs a Business Card Design

***We want a very sharp and unforgettable pantone for the Business Card. ***
***We do not want the business card or logo only in black, white and grey color!!!Please provide us a main color as our brand topic! Thanks!! ***

Mabel’s Nook is a Hong Kong based fine jewelry brand.

We want a very nice, simple and elegant business card design for Mabel's Nook Brand. The company's logo has been uploaded already.

You can design with below info:

Dorian Fung
Director
M: +852 94273658
T: +852 35820417
F: +852 35820419
E: dorian.fung@mabelsnook.example
5/F , Harbourlight Tower, 12-18 Orchid Lane, Wan Tung Kok, Kowloon, Hong Kong

Target Market(s)

Mabel’s Nook philosophy is a jewelry icon of young, creative, trendy, fashionable, stylish, energetic, and elegant. For Mabel’s Nook, jewelry is one collection of artworks, the most important items in personal life.

Industry/Entity Type

Jewelry

Requirements
Must have
• We want a very sharp and unforgettable pantone for the Business Card.

```html
<!DOCTYPE html>
<html lang="en">
<head>
<meta charset="utf-8">
<title>Mabel’s Nook — Business Card</title>
<link rel="stylesheet" href="https://fonts.googleapis.com/css2?family=Cinzel:wght@400;500&family=Cormorant+Garamond:wght@400;500&display=swap">
<style>
  :root {
    --backdrop: #e9e6e1;
    --card-black: #1f1f1f;
    --band-black: #232323;
    --gold: #a8864a;
    --gold-deep: #7d6232;
    --ink-light: #f2f0ec;
    --ink-soft: #d6d3cd;
  }
  * { box-sizing: border-box; margin: 0; padding: 0; }
  html, body {
    width: 1200px; height: 900px; overflow: hidden;
    background: var(--backdrop);
  }
  .sheet {
    width: 1200px; height: 900px;
    display: flex; flex-direction: column;
    align-items: center; justify-content: center; gap: 56px;
  }
  .card {
    position: relative;
    width: 620px; height: 372px;
    background: var(--card-black);
    box-shadow: 0 10px 28px rgba(0,0,0,.18);
    overflow: hidden;
  }

  /* Back side: patterned field with brand band */
  .pattern-field {
    position: absolute; left: 0; right: 0;
    background: linear-gradient(135deg, var(--gold-deep), #5b4829 50%, var(--gold-deep));
  }
  .pattern-field--top { top: 0; height: 138px; }
  .pattern-field--bottom { bottom: 0; height: 138px; }
  .brand-band {
    position: absolute; left: 0; right: 0; top: 138px; height: 96px;
    background: var(--band-black);
    display: flex; align-items: center; justify-content: center;
  }
  .brand-band__name {
    font-family: "Cinzel", serif; font-weight: 400;
    font-size: 30px; letter-spacing: 5px;
    color: var(--gold);
  }

  /* Front side: contact details */
  .holder {
    position: absolute; left: 46px; top: 150px;
  }
  .holder__name {
    font-family: "Cinzel", serif; font-weight: 400;
    font-size: 26px; letter-spacing: 2px;
    color: var(--ink-light);
  }
  .holder__role {
    font-family: "Cormorant Garamond", serif;
    font-size: 16px; color: var(--ink-soft); margin-top: 2px;
  }
  .contact {
    position: absolute; left: 350px; top: 40px;
    font-family: "Cormorant Garamond", serif;
    font-size: 14.5px; line-height: 19px; color: var(--ink-soft);
  }
  .contact__row { display: flex; }
  .contact__label { width: 22px; color: var(--gold); }
  .address {
    position: absolute; left: 372px; top: 146px;
    font-family: "Cormorant Garamond", serif;
    font-size: 14.5px; line-height: 19px; color: var(--ink-soft);
  }
  .website {
    position: absolute; right: 46px; top: 262px;
    font-family: "Cormorant Garamond", serif;
    font-size: 14.5px; color: var(--gold);
  }
  .brand-mark {
    position: absolute; left: 170px; top: 222px;
    display: flex; flex-direction: column; align-items: center; gap: 14px;
  }
  .brand-mark__disc {
    width: 80px; height: 80px; border-radius: 50%;
    background: var(--gold);
  }
  .brand-mark__name {
    font-family: "Cinzel", serif; font-weight: 400;
    font-size: 18px; letter-spacing: 2.5px; color: var(--gold);
  }
</style>
</head>
<body>
<main class="sheet">

  <section class="card card--back" aria-label="Card back">
    <div class="pattern-field pattern-field--top" role="img" aria-label="Gold lattice pattern on black"></div>
    <div class="brand-band">
      <span class="brand-band__name">Mabel’s Nook</span>
    </div>
    <div class="pattern-field pattern-field--bottom" role="img" aria-label="Gold lattice pattern on black"></div>
  </section>

  <section class="card card--front" aria-label="Card front">
    <div class="contact">
      <div class="contact__row"><span class="contact__label">M</span><span>+852 94273658</span></div>
      <div class="contact__row"><span class="contact__label">T</span><span>+852 35820417</span></div>
      <div class="contact__row"><span class="contact__label">F</span><span>+852 35820419</span></div>
      <div class="contact__row"><span class="contact__label">E</span><span>dorian.fung@mabelsnook.example</span></div>
    </div>
    <address class="address" style="font-style:normal">
      5/F Harbourlight Tower,<br>
      12-18 Orchid Lane,<br>
      Wan Tung Kok, Kowloon,<br>
      Hong Kong
    </address>
    <div class="website">www.mabelsnook.example</div>

    <div class="holder">
      <div class="holder__name">Dorian Fung</div>
      <div class="holder__role">Director</div>
    </div>

    <div class="brand-mark">
      <div class="brand-mark__disc"></div>
      <div class="brand-mark__name">Mabel’s Nook</div>
    </div>
  </section>

</main>
</body>
</html>
```